Honey apple cider vinegar label

organic food company need a contemporary honey apple cider vinegar and honey vinegar label, natural GMP logo HACCP LOgo
label detail height :140mm Width:80mm
ingredient: honey, apple cider vinegar and water, free from artificial color & preservative
Shelf Life: 3 years
Net weight 400ml
Storage : store in cool place , do not expose to sunlight
instruction for use: add 20ml to a full glass of water 3, times a days before meal, stop consuming if allergies happen
certification, GMP HACCP, Halal, natural product

Target Market(s)

health conscious group

Requirements
Must have
• modern feel, honey and apple picture

```html
<!DOCTYPE html>
<html lang="en">
<head>
<meta charset="utf-8">
<title>Honey Apple Cider Vinegar Label</title>
<link rel="stylesheet" href="https://fonts.googleapis.com/css2?family=Alfa+Slab+One&family=Lobster&family=Lobster+Two:ital,wght@1,700&family=Open+Sans:wght@300;600&display=swap">
<style>
  :root {
    --orange: #e8650a;
    --gold: #f9ac28;
    --gold-soft: #f6a623;
    --brand-ink: #2d1b3d;
    --paper: #ffffff;
    --canvas: #ffffff;
    --navy: #2c3a8c;
  }
  html, body {
    margin: 0;
    padding: 0;
    width: 1200px;
    height: 1200px;
    overflow: hidden;
    background: var(--canvas);
  }
  .sheet { display: block; width: 1200px; height: 1200px; }
  .frame-outer { fill: var(--paper); stroke: var(--orange); stroke-width: 9; }
  .frame-inner { fill: none; stroke: var(--gold); stroke-width: 5; }
  .brand-name { font-family: "Open Sans", sans-serif; font-weight: 600; font-size: 50px; fill: var(--brand-ink); }
  .brand-dot { fill: var(--gold); }
  .tagline { font-family: "Lobster Two", cursive; font-style: italic; font-weight: 700; font-size: 40px; fill: var(--gold-soft); }
  .product-name { font-family: "Lobster", cursive; font-size: 76px; fill: var(--orange); }
  .info { font-family: "Open Sans", sans-serif; font-weight: 300; font-size: 26px; fill: var(--orange); }
  .info-storage { fill: var(--gold); }
  .info-light { fill: #ffffff; }
  .volume { font-family: "Alfa Slab One", serif; font-size: 92px; fill: var(--orange); }
  .volume-small { font-family: "Alfa Slab One", serif; font-size: 56px; fill: var(--orange); }
  .volume-unit { font-family: "Lobster Two", cursive; font-style: italic; font-weight: 700; font-size: 58px; fill: var(--orange); }
  .shelf-life { font-family: "Open Sans", sans-serif; font-weight: 300; font-size: 28px; fill: var(--orange); }
  .shelf-life-gold { fill: var(--gold); }
  .badge { fill: var(--paper); stroke: var(--orange); stroke-width: 4; }
  .badge-core { fill: var(--orange); }
  .badge-core-navy { fill: var(--navy); }
  .band-orange { fill: var(--orange); }
  .band-gold { fill: var(--gold); }
</style>
</head>
<body>
<svg class="sheet" viewBox="0 0 1932 1932" xmlns="http://www.w3.org/2000/svg">
  <defs>
    <path id="label-shape" d="M586 290 C470 290 420 340 372 392 C334 432 296 448 274 460 C262 468 262 480 266 492 C306 700 322 840 322 966 C322 1092 306 1232 266 1440 C262 1452 262 1464 274 1472 C296 1484 334 1500 372 1540 C420 1592 470 1642 586 1642 C702 1642 752 1592 800 1540 C838 1500 876 1484 898 1472 C910 1464 910 1452 906 1440 C866 1232 850 1092 850 966 C850 840 866 700 906 492 C910 480 910 468 898 460 C876 448 838 432 800 392 C752 340 702 290 586 290 Z"/>
    <clipPath id="label-clip"><use href="#label-shape"/></clipPath>
    <linearGradient id="jar-fill" x1="0" y1="0" x2="1" y2="1">
      <stop offset="0" stop-color="#e9c89a"/>
      <stop offset="0.45" stop-color="#f5a21c"/>
      <stop offset="1" stop-color="#c9261c"/>
    </linearGradient>
    <g id="label-frame">
      <use href="#label-shape" class="frame-outer"/>
      <use href="#label-shape" class="frame-inner" transform="translate(586 966) scale(0.94 0.966) translate(-586 -966)" vector-effect="non-scaling-stroke"/>
    </g>
    <g id="label-header">
      <circle class="brand-dot" cx="586" cy="364" r="20"/>
      <text class="brand-name" x="582" y="426" text-anchor="middle">Orchardia</text>
      <rect role="img" aria-label="Illustration of a honey jar with a cloth lid and daisy beside a red apple" x="425" y="455" width="340" height="335" rx="150" fill="url(#jar-fill)"/>
      <text class="tagline" x="585" y="838" text-anchor="middle" textLength="280" lengthAdjust="spacingAndGlyphs">organic &amp; natural</text>
      <text class="product-name" x="580" y="922" text-anchor="middle" textLength="440" lengthAdjust="spacingAndGlyphs">Honey Apple Cider</text>
      <text class="product-name" x="573" y="1000" text-anchor="middle" textLength="230" lengthAdjust="spacingAndGlyphs">Vinegar</text>
    </g>
    <g id="label-volume">
      <text class="volume" x="478" y="1432" textLength="106" lengthAdjust="spacingAndGlyphs">40</text>
      <text class="volume-small" x="586" y="1412" textLength="36" lengthAdjust="spacingAndGlyphs">0</text>
      <text class="volume-unit" x="628" y="1410" textLength="62" lengthAdjust="spacingAndGlyphs">ml</text>
    </g>
    <g id="label-badges">
      <circle class="badge" cx="484" cy="1530" r="50"/>
      <circle class="badge-core" cx="484" cy="1530" r="30"/>
      <circle class="badge" cx="591" cy="1530" r="50"/>
      <circle class="badge-core badge-core-navy" cx="591" cy="1530" r="30"/>
      <polygon class="badge" points="692,1480 712,1496 738,1496 738,1520 754,1530 738,1540 738,1564 712,1564 692,1580 672,1564 646,1564 646,1540 630,1530 646,1520 646,1496 672,1496"/>
    </g>
  </defs>

  <g class="label label-plain">
    <use href="#label-frame"/>
    <use href="#label-header"/>
    <g class="label-details">
      <text class="info" x="588" y="1058" text-anchor="middle" textLength="460" lengthAdjust="spacingAndGlyphs">ingredient: honey, apple cider vinegar and</text>
      <text class="info" x="588" y="1091" text-anchor="middle" textLength="352" lengthAdjust="spacingAndGlyphs">water, free from artificial color &amp;</text>
      <text class="info" x="588" y="1124" text-anchor="middle" textLength="135" lengthAdjust="spacingAndGlyphs">preservative</text>
      <text class="info info-storage" x="589" y="1164" text-anchor="middle" textLength="210" lengthAdjust="spacingAndGlyphs">store in cool place ,</text>
      <text class="info info-storage" x="589" y="1197" text-anchor="middle" textLength="278" lengthAdjust="spacingAndGlyphs">do not expose to sunlight</text>
      <text class="info" x="587" y="1238" text-anchor="middle" textLength="206" lengthAdjust="spacingAndGlyphs">instruction for use:</text>
      <text class="info" x="587" y="1271" text-anchor="middle" textLength="347" lengthAdjust="spacingAndGlyphs">add 20ml to a full glass of water</text>
      <text class="info" x="590" y="1304" text-anchor="middle" textLength="300" lengthAdjust="spacingAndGlyphs">3 times a days before meal,</text>
      <text class="info" x="587" y="1338" text-anchor="middle" textLength="381" lengthAdjust="spacingAndGlyphs">stop consuming if allergies happen</text>
    </g>
    <use href="#label-volume"/>
    <text class="shelf-life" x="589" y="1470" text-anchor="middle" textLength="198" lengthAdjust="spacingAndGlyphs">Shelf Life: 3 years</text>
    <use href="#label-badges"/>
  </g>

  <g class="label label-banded" transform="translate(740 0)">
    <use href="#label-frame"/>
    <g class="info-bands" clip-path="url(#label-clip)">
      <rect class="band-orange" x="305" y="1022" width="562" height="116"/>
      <rect class="band-gold" x="318" y="1138" width="534" height="70"/>
      <rect class="band-orange" x="260" y="1211" width="652" height="141"/>
    </g>
    <use href="#label-header"/>
    <g class="label-details">
      <text class="info info-light" x="588" y="1058" text-anchor="middle" textLength="460" lengthAdjust="spacingAndGlyphs">ingredient: honey, apple cider vinegar and</text>
      <text class="info info-light" x="588" y="1091" text-anchor="middle" textLength="352" lengthAdjust="spacingAndGlyphs">water, free from artificial color &amp;</text>
      <text class="info info-light" x="588" y="1124" text-anchor="middle" textLength="135" lengthAdjust="spacingAndGlyphs">preservative</text>
      <text class="info info-light" x="589" y="1164" text-anchor="middle" textLength="210" lengthAdjust="spacingAndGlyphs">store in cool place ,</text>
      <text class="info info-light" x="589" y="1197" text-anchor="middle" textLength="278" lengthAdjust="spacingAndGlyphs">do not expose to sunlight</text>
      <text class="info info-light" x="587" y="1238" text-anchor="middle" textLength="206" lengthAdjust="spacingAndGlyphs">instruction for use:</text>
      <text class="info info-light" x="587" y="1271" text-anchor="middle" textLength="347" lengthAdjust="spacingAndGlyphs">add 20ml to a full glass of water</text>
      <text class="info info-light" x="590" y="1304" text-anchor="middle" textLength="300" lengthAdjust="spacingAndGlyphs">3 times a days before meal,</text>
      <text class="info info-light" x="587" y="1338" text-anchor="middle" textLength="381" lengthAdjust="spacingAndGlyphs">stop consuming if allergies happen</text>
    </g>
    <use href="#label-volume"/>
    <text class="shelf-life shelf-life-gold" x="589" y="1470" text-anchor="middle" textLength="198" lengthAdjust="spacingAndGlyphs">Shelf Life: 3 years</text>
    <use href="#label-badges"/>
  </g>
</svg>
</body>
</html>
```